Zest Owl Gig - 20 Years of Funk

I'm with a funk band called Zest Owl. We are celebrating our 20 year anniversary with a show on August 3, 2024. We would like some banners made for social media to help promote the gig. I'm attaching some examples of our 10 year anniversary gig so you can at least get an idea of what we are looking for.

Here's the text for the banners:
ZEST OWL Anniversary Gig - 20 Years of Funk!
Saturday, August 10, 2024
with special guest: Marco Delvine
Doors at 7pm, Show at 8pm

We would like three sizes:
1920 x 1005 pixels
1080 x 1080 pixels
1080 x 1920 pixels

You can check out our website for more ideas of our graphic style, etc.. www.zestowlgroove.com

```html
<!DOCTYPE html>
<html lang="en">
<head>
<meta charset="utf-8">
<title>Zest Owl – 20 Years of Funk Banners</title>
<link href="https://fonts.googleapis.com/css2?family=Montserrat:wght@400;500;700;800&family=Titan+One&family=Lobster&family=Great+Vibes&display=swap" rel="stylesheet">
<style>
  :root {
    --stage: #e4e4e4;
    --purple: #8a1fb0;
    --pink: #e93a9f;
    --teal: rgba(34, 196, 182, 0.8);
    --violet: rgba(96, 52, 196, 0.7);
    --night: #2d0d5c;
    --night-deep: #260a4e;
    --lime: #c8e022;
    --ink: #111;
    --white: #ffffff;
  }
  * { margin: 0; padding: 0; box-sizing: border-box; }
  html, body { width: 1200px; height: 1200px; overflow: hidden; }
  body { background: var(--stage); position: relative; font-family: "Montserrat", sans-serif; }

  .banner {
    position: absolute;
    overflow: hidden;
    background:
      linear-gradient(180deg, transparent 0%, transparent var(--t0, 28%), var(--teal) var(--t1, 44%), var(--violet) var(--t2, 56%), var(--night) var(--t3, 70%), var(--night-deep) 100%),
      linear-gradient(90deg, var(--purple), var(--pink));
  }
  .banner > * { position: absolute; }

  .band-photo {
    background: linear-gradient(180deg, rgba(90,90,98,0.7) 0%, rgba(170,172,180,0.7) 50%, rgba(110,200,210,0.4) 80%, rgba(110,200,210,0) 100%);
  }

  .wordmark { font-family: "Montserrat", sans-serif; font-weight: 800; color: var(--lime); white-space: nowrap; }
  .badge { border-radius: 50%; background: #0c0c0c; border: solid var(--lime); display: flex; align-items: center; justify-content: center; }
  .badge .wordmark { position: static; }

  .script { font-family: "Great Vibes", cursive; color: var(--white); white-space: nowrap; line-height: 1; text-shadow: 1px 1px 0 rgba(0,0,0,0.35); }
  .gig { font-family: "Titan One", sans-serif; color: var(--lime); line-height: 1; text-shadow: 2px 2px 0 rgba(0,0,0,0.35); }
  .twenty { font-family: "Titan One", sans-serif; color: var(--lime); line-height: 1; text-shadow: 3px 3px 0 var(--ink); }
  .years { font-family: "Lobster", cursive; color: var(--lime); line-height: 1; text-shadow: 3px 3px 0 var(--ink); white-space: nowrap; }
  .of-funk { color: var(--white); font-style: italic; line-height: 1; white-space: nowrap; }
  .of-funk b { font-weight: 800; }

  .date { color: var(--white); line-height: 1.05; font-weight: 500; }
  .date strong { display: block; color: var(--lime); font-weight: 800; }
  .divider { background: var(--white); width: 1.5px; }
  .guest-label { color: var(--white); line-height: 1.2; }
  .guest-name { color: var(--lime); font-weight: 800; line-height: 1.15; }

  .doors { background: var(--lime); color: var(--ink); display: flex; align-items: center; justify-content: center; white-space: nowrap; }
  .doors b { font-weight: 800; margin: 0 0.25em; }
</style>
</head>
<body>

<!-- Portrait banner -->
<section class="banner banner--portrait" style="left:87px;top:227px;width:352px;height:626px;--t0:20%;--t1:38%;--t2:52%;--t3:66%;">
  <div class="wordmark" style="left:0;width:352px;top:40px;font-size:50px;text-align:center;">Zest Owl</div>
  <div class="band-photo" role="img" aria-label="Black and white photo of the band performing: trumpet player, singer at a microphone and guitarist" style="left:0;top:130px;width:352px;height:200px;"></div>
  <div class="script" style="left:22px;top:318px;font-size:48px;">Aniversary</div>
  <div class="gig" style="left:223px;top:322px;font-size:62px;">GIG</div>
  <div class="twenty" style="left:33px;top:414px;font-size:58px;">20</div>
  <div class="of-funk" style="left:219px;top:394px;font-size:17px;">of <b>Funk!</b></div>
  <div class="years" style="left:142px;top:410px;font-size:62px;">Years</div>
  <div class="date" style="left:33px;top:496px;font-size:14px;">SATURDAY,<strong style="font-size:17px;">AUGUST<br>10, 2024</strong></div>
  <div class="divider" style="left:133px;top:496px;height:58px;"></div>
  <div class="guest-label" style="left:145px;top:496px;font-size:15px;">With<br>Special<br>Guest:</div>
  <div class="guest-name" style="left:213px;top:494px;font-size:22px;">Marco<br>Delvine</div>
  <div class="doors" style="left:34px;top:561px;width:283px;height:31px;font-size:16px;">Doors at <b>7pm, SHOW</b> at <b>8pm</b></div>
</section>

<!-- Landscape banner -->
<section class="banner banner--landscape" style="left:487px;top:227px;width:626px;height:328px;--t0:18%;--t1:34%;--t2:50%;--t3:64%;">
  <div class="band-photo" role="img" aria-label="Black and white photo of the band performing: trumpet player, singer at a microphone and bass guitarist" style="left:96px;top:13px;width:430px;height:175px;"></div>
  <div class="script" style="left:34px;top:166px;font-size:52px;">Aniversary</div>
  <div class="gig" style="left:82px;top:222px;font-size:74px;">GIG</div>
  <div class="badge" style="left:274px;top:181px;width:104px;height:104px;border-width:7px;">
    <span class="wordmark" style="font-size:15px;">Zest Owl</span>
  </div>
  <div class="twenty" style="left:394px;top:174px;font-size:44px;">20</div>
  <div class="of-funk" style="left:530px;top:162px;font-size:13px;">of <b>Funk!</b></div>
  <div class="years" style="left:476px;top:176px;font-size:46px;">Years</div>
  <div class="date" style="left:394px;top:236px;font-size:11px;">SATURDAY,<strong style="font-size:13px;">AUGUST<br>10, 2024</strong></div>
  <div class="divider" style="left:462px;top:236px;height:42px;"></div>
  <div class="guest-label" style="left:472px;top:235px;font-size:11.5px;">With<br>Special<br>Guest:</div>
  <div class="guest-name" style="left:522px;top:233px;font-size:17px;">Marco<br>Delvine</div>
  <div class="doors" style="left:395px;top:284px;width:199px;height:20px;font-size:11.5px;">Doors at <b>7pm, SHOW</b> at <b>8pm</b></div>
</section>

<!-- Square banner -->
<section class="banner banner--square" style="left:487px;top:620px;width:352px;height:352px;--t0:22%;--t1:40%;--t2:56%;--t3:70%;">
  <div class="band-photo" role="img" aria-label="Black and white photo of the band performing: trumpet player, singer at a microphone and bass guitarist" style="left:0;top:80px;width:352px;height:130px;"></div>
  <div class="script" style="left:23px;top:22px;font-size:46px;">Aniversary</div>
  <div class="gig" style="left:222px;top:26px;font-size:58px;">GIG</div>
  <div class="badge" style="left:35px;top:219px;width:90px;height:90px;border-width:6px;">
    <span class="wordmark" style="font-size:13px;">Zest Owl</span>
  </div>
  <div class="twenty" style="left:144px;top:214px;font-size:38px;">20</div>
  <div class="of-funk" style="left:262px;top:204px;font-size:11.5px;">of <b>Funk!</b></div>
  <div class="years" style="left:212px;top:216px;font-size:40px;">Years</div>
  <div class="date" style="left:144px;top:268px;font-size:9.5px;">SATURDAY,<strong style="font-size:11.5px;">AUGUST<br>10, 2024</strong></div>
  <div class="divider" style="left:204px;top:268px;height:37px;"></div>
  <div class="guest-label" style="left:211px;top:267px;font-size:10px;">With<br>Special<br>Guest:</div>
  <div class="guest-name" style="left:253px;top:265px;font-size:15px;">Marco<br>Delvine</div>
  <div class="doors" style="left:144px;top:310px;width:171px;height:19px;font-size:10px;">Doors at <b>7pm, SHOW</b> at <b>8pm</b></div>
</section>

</body>
</html>
```